Road Construction Company needs business cards

We would like a new business card designed for our business.

We're a road construction company based in Qld, Australia.

Can the business card please have the following information on it.

Name: Brent Malvoy
Position: General Manager
Phone: 0471 592 304
Email: Brent.malvoy@quendix.com.au
Address: 87 Harrowgate Ave, Pindarra, QLD, 4000
Website: www.quendix.com.au

Visually we'd like the card to be professional and simple.

Attached is our logo.

Our website is www.quendix.com.au

Target Market(s)

Men aged 25-60

Contact Information for Business Card

As listed in project description

Font styles to use
Serif

Requirements
Must have
• Large logo on back of card

```html
<!DOCTYPE html>
<html lang="en">
<head>
<meta charset="utf-8">
<title>Quendix Business Card</title>
<link rel="stylesheet" href="https://fonts.googleapis.com/css2?family=Poppins:wght@400;600;700&display=swap">
<style>
  :root {
    --brand-blue: #0455a6;
    --sky-blue: #2fa3d9;
    --ink-grey: #5a5f66;
    --paper: #ffffff;
    --backdrop: #e9ebee;
  }
  html, body {
    margin: 0;
    width: 1200px;
    height: 900px;
    overflow: hidden;
    background: var(--backdrop);
    font-family: "Poppins", sans-serif;
  }
  .card {
    position: absolute;
    width: 700px;
    height: 400px;
    box-shadow: 0 6px 18px rgba(0,0,0,0.18);
    overflow: hidden;
  }
  .card--front {
    left: 150px;
    top: 35px;
    background: var(--brand-blue);
    display: flex;
    align-items: center;
    justify-content: center;
  }
  .card--back {
    left: 350px;
    top: 465px;
    background: var(--paper);
  }
  .wordmark {
    display: flex;
    align-items: center;
    gap: 14px;
    font-weight: 700;
    letter-spacing: 2px;
    line-height: 1;
  }
  .wordmark__square {
    width: 0.55em;
    height: 0.55em;
    background: currentColor;
  }
  .card--front .wordmark {
    color: var(--paper);
    font-size: 72px;
  }
  .card--back .wordmark {
    position: absolute;
    left: 70px;
    top: 168px;
    color: var(--brand-blue);
    font-size: 46px;
  }
  .divider {
    position: absolute;
    left: 348px;
    top: 70px;
    width: 2px;
    height: 215px;
    background: var(--brand-blue);
  }
  .details {
    position: absolute;
    left: 378px;
    top: 62px;
    color: var(--ink-grey);
    font-size: 15px;
    line-height: 1.45;
  }
  .details__name {
    margin: 0;
    color: var(--brand-blue);
    font-size: 28px;
    font-weight: 700;
    line-height: 1.1;
    text-transform: uppercase;
  }
  .details__role {
    margin: 2px 0 14px;
    font-size: 16px;
    text-transform: uppercase;
  }
  .details__address { margin: 0 0 12px; }
  .contact-list { list-style: none; margin: 0; padding: 0; }
  .contact-list li { display: flex; align-items: center; gap: 8px; }
  .contact-list svg { width: 13px; height: 13px; flex: none; }
  .card__bands {
    position: absolute;
    left: 0;
    bottom: 0;
    width: 700px;
    height: 40px;
  }
</style>
</head>
<body>
  <section class="card card--front">
    <div class="wordmark"><span class="wordmark__square"></span>QUENDIX</div>
  </section>

  <section class="card card--back">
    <div class="wordmark"><span class="wordmark__square"></span>QUENDIX</div>
    <div class="divider"></div>
    <div class="details">
      <h1 class="details__name">Brent Malvoy</h1>
      <p class="details__role">General Manager</p>
      <p class="details__address">87 Harrowgate Ave,<br>Pindarra, QLD, 4000</p>
      <ul class="contact-list">
        <li>
          <svg viewBox="0 0 16 16" aria-hidden="true"><path d="M4 1l3 3-2 2c1 2 3 4 5 5l2-2 3 3-2 3C7 14 2 9 1 3z" fill="var(--brand-blue)"/></svg>
          0471 592 304
        </li>
        <li>
          <svg viewBox="0 0 16 16" aria-hidden="true"><rect x="1" y="3" width="14" height="10" fill="none" stroke="var(--brand-blue)" stroke-width="1.6"/><path d="M1 3l7 6 7-6" fill="none" stroke="var(--brand-blue)" stroke-width="1.6"/></svg>
          Brent.malvoy@quendix.com.au
        </li>
        <li>
          <svg viewBox="0 0 16 16" aria-hidden="true"><circle cx="8" cy="8" r="6.5" fill="none" stroke="var(--brand-blue)" stroke-width="1.5"/><path d="M1.5 8h13M8 1.5c-3 3.5-3 9.5 0 13M8 1.5c3 3.5 3 9.5 0 13" fill="none" stroke="var(--brand-blue)" stroke-width="1.2"/></svg>
          www.quendix.com.au
        </li>
      </ul>
    </div>
    <svg class="card__bands" viewBox="0 0 700 40" preserveAspectRatio="none" aria-hidden="true">
      <polygon points="0,28 455,28 447,40 0,40" fill="var(--brand-blue)"/>
      <polygon points="468,10 700,10 700,40 452,40" fill="var(--sky-blue)"/>
    </svg>
  </section>
</body>
</html>
```